Kellwood Build, Carpentry Services

Business card for carpentry business in the Sunshine Coast.

Business card layout required using logo provided - provided both PDF copy and AI. Please let me know if you would like a the files for the logo symbol and text by itself.

Business Colours are grey, blue and white. The font colours codes for this design are Blue Hex # 00B4E6 and Hex # 39393B for the gray colour.

FYI font for logo is Gotham Bold.

Preference for a clean and striking layout that is simple and elegant.

Target Market(s)

Young Families, retirees, young couples requiring assistance with small to medium works/renovations on the Sunshine Coast.

Industry/Entity Type

Construction

Contact Information for Business Card

Dean Kellwood
Carpenter
0489305627
dean@kellwoodbuild.com.au
Coralby Heads, Tidewater Coast
RHPA Licensed Carpenter (In smaller font)

Font styles to use
Sans Serif

Colors

Designer to choose colors to be used in the design.

Requirements
Must have
• Logo provided must appear on the card, preferably on one side of the card by itself with the text on the alternate side
Nice to have
• Text on the other side of card, maybe grey background and white font here but happy for the designer to provide ideas here.
Should not have
• Use of other colours, other than the ones provided - white, grey and blue. Black optional.

```html
<!DOCTYPE html>
<html lang="en">
<head>
<meta charset="utf-8">
<title>Kellwood Build — Business Card</title>
<link rel="stylesheet" href="https://fonts.googleapis.com/css2?family=Montserrat:wght@700&family=Roboto:wght@300;400&display=swap">
<style>
  :root {
    --blue: #00B4E6;
    --grey: #39393B;
    --grey-dark: #26262a;
    --white: #ffffff;
    --text-soft: #e6e6e8;
    --rule: #bdbdc0;
    --backdrop: #2b2522;
  }
  * { margin: 0; padding: 0; box-sizing: border-box; }
  html, body {
    width: 1200px; height: 716px; overflow: hidden;
    background: var(--backdrop);
  }
  .canvas {
    position: relative; width: 1200px; height: 716px;
    display: flex; align-items: center; justify-content: center; gap: 40px;
  }
  .card {
    position: relative; width: 540px; height: 330px;
    border-left: 3px solid var(--blue);
    border-bottom: 3px solid var(--blue);
    box-shadow: 0 14px 30px rgba(0,0,0,.45);
    overflow: hidden;
  }

  /* Shared brand lockup */
  .brand { position: absolute; display: flex; flex-direction: column; }
  .brand__row { display: flex; align-items: center; gap: 10px; }
  .brand__mark { width: 14px; height: 14px; background: var(--blue); flex: none; }
  .brand__name {
    font-family: "Montserrat", sans-serif; font-weight: 700;
    color: var(--blue); letter-spacing: .04em; white-space: nowrap; line-height: 1.1;
  }
  .brand__tag {
    font-family: "Roboto", sans-serif; font-weight: 400;
    color: var(--white); letter-spacing: .3em; text-transform: uppercase;
    border-top: 1px solid var(--white); margin-left: 24px; padding-top: 4px;
    white-space: nowrap;
  }

  /* Front */
  .card--front { background: var(--grey-dark); }
  .card__pattern {
    position: absolute; inset: 0;
    background: linear-gradient(120deg, #1e1e21 0%, #2c2c30 45%, #4a4a4f 100%);
  }
  .card--front .brand { left: 140px; top: 160px; }
  .card--front .brand__name { font-size: 26px; }
  .card--front .brand__tag { font-size: 8px; }

  /* Back */
  .card--back { background: var(--grey); color: var(--text-soft); font-family: "Roboto", sans-serif; }
  .card--back .brand { right: 28px; top: 44px; align-items: flex-end; }
  .card--back .brand__name { font-size: 20px; }
  .card--back .brand__tag { font-size: 7px; }
  .person { position: absolute; left: 34px; top: 128px; }
  .person__name {
    font-family: "Montserrat", sans-serif; font-weight: 700;
    color: var(--blue); font-size: 19px; text-transform: uppercase; letter-spacing: .01em;
  }
  .person__role { font-weight: 300; font-size: 12px; margin-top: 2px; }
  .divider {
    position: absolute; left: 34px; right: 34px; top: 190px;
    height: 1px; background: var(--rule);
  }
  .contact { position: absolute; left: 34px; top: 204px; list-style: none; font-weight: 300; font-size: 12px; }
  .contact li { display: flex; align-items: center; gap: 8px; margin-bottom: 5px; }
  .contact svg { width: 11px; height: 11px; fill: var(--blue); }
  .location { position: absolute; right: 34px; bottom: 30px; text-align: right; }
  .location__place { font-weight: 300; font-size: 13px; }
  .location__licence { font-weight: 300; font-size: 10px; color: var(--blue); margin-top: 2px; }
</style>
</head>
<body>
<main class="canvas">
  <section class="card card--front">
    <div class="card__pattern" role="img" aria-label="Repeating tonal pattern of embossed house symbols across the card face"></div>
    <div class="brand">
      <div class="brand__row">
        <span class="brand__mark"></span>
        <span class="brand__name">KELLWOOD BUILD</span>
      </div>
      <span class="brand__tag">Carpentry Services</span>
    </div>
  </section>

  <section class="card card--back">
    <div class="brand">
      <div class="brand__row">
        <span class="brand__mark"></span>
        <span class="brand__name">KELLWOOD BUILD</span>
      </div>
      <span class="brand__tag">Carpentry Services</span>
    </div>
    <div class="person">
      <h1 class="person__name">Dean Kellwood</h1>
      <p class="person__role">Carpenter</p>
    </div>
    <div class="divider"></div>
    <ul class="contact">
      <li>
        <svg viewBox="0 0 24 24" aria-hidden="true"><path d="M6.6 10.8a15.1 15.1 0 0 0 6.6 6.6l2.2-2.2a1 1 0 0 1 1-.25 11.4 11.4 0 0 0 3.6.57 1 1 0 0 1 1 1V20a1 1 0 0 1-1 1A17 17 0 0 1 3 4a1 1 0 0 1 1-1h3.5a1 1 0 0 1 1 1c0 1.25.2 2.45.57 3.57a1 1 0 0 1-.25 1z"/></svg>
        0489305627
      </li>
      <li>
        <svg viewBox="0 0 24 24" aria-hidden="true"><path d="M2 5h20v14H2zM4 7v.5l8 5 8-5V7l-8 5z"/></svg>
        dean@kellwoodbuild.com.au
      </li>
    </ul>
    <div class="location">
      <p class="location__place">Coralby Heads, Tidewater Coast</p>
      <p class="location__licence">RHPA Licensed Carpenter</p>
    </div>
  </section>
</main>
</body>
</html>
```